Personal Finance Author needs a postcard

Hi there,

I am a Canadian personal finance author and have published a new book called The Coin Keeper.

I teach Millennials how to create a 6-figure portfolio through investing (https://www.miradabbot.example/)

I'm speaking at some conferences so we were going to print some postcards to hand out to attendees with our info and calls-to-action on them.

I am looking for 4x6 (horizontal) postcard (no space needed for shipping label).

Logos, Headshots and Book Cover:
https://files.example.net/share/9ZqLp72WxTbVn4KcRd0sHj3aE5uYgMfo?view=open

Both sides will be full colour. I would like a clean and simple look. Our main sites are www.MiraDabbot.example and www.TheCoinKeeperBook.example if you want to get a sense of style and design.
I also uploaded a few marketing materials so you can see the existing designs.

Side 1:
Get Instant Access to your Free Resources - main headline

(small bullets underneath)
- The Coin Keeper Checklist
- Financial Worksheets
- Database of Investment Tools

MiraDabbot.example/Resources

At the bottom, include "Don't forget to follow Mira Dabbot on social media:
Linkedin: @miradabbot7
Facebook: @thecoinkeeperbook Instagram: @thecoinkeeperbook Twitter: @CoinKeeperBook"

Side 2:
Headline - Want to work directly with Mira and The Coin Keeper team to help you make your money grow and stay safe?

Work with us to (bullet point list)...
- Hire Mira as a Keynote Speaker
- Teach Financial Literacy Workshops
- Receive Financial Coaching

Want To Learn More About How We Can Help?
MiraDabbot.example/Services

Include my contact info:
Mira Dabbot
Author | Speaker | Investor
mira@thecoinkeeperbook.example
555-274-0381

Target Market(s)

Millennials who want to learn how to save and invest their money. I focus on stock market investing, real estate investing and entrepreneurship.

Industry/Entity Type

Financial Service

Font styles to use
Sans Serif

Colors

Designer to choose colors to be used in the design.

Requirements
Must have
• Photo of Mira Dabbot
• The Coin Keeper logo
• Green, Gold/Yellow to match existing colours
• modern business style postcard

```html
<!DOCTYPE html>
<html lang="en">
<head>
<meta charset="utf-8">
<title>The Coin Keeper Postcard</title>
<link rel="stylesheet" href="https://fonts.googleapis.com/css2?family=Bebas+Neue&family=Lato:ital,wght@0,400;0,700;1,400&family=Roboto:wght@400;700&display=swap">
<style>
:root{
  --green:#0f6a33;
  --green-dark:#0b4f26;
  --gold:#e9b234;
  --gold-light:#f7d77a;
  --ink:#1d1d1d;
  --white:#ffffff;
  --page:#e6e6e6;
  --photo:#3a3540;
  --book:#e9efe6;
}
*{margin:0;padding:0;box-sizing:border-box}
html,body{width:902px;height:1200px;overflow:hidden;background:var(--page)}
.canvas{position:relative;width:902px;height:1200px}
.card{position:absolute;width:608px;height:412px;background:var(--white);overflow:hidden;box-shadow:0 6px 14px rgba(0,0,0,.25)}
.card--front{left:58px;top:144px}
.card--back{left:204px;top:667px}
.card svg.shapes{position:absolute;left:0;top:0}
.abs{position:absolute}
.display{font-family:"Bebas Neue",Impact,sans-serif;line-height:1;font-weight:400}
.headline-front{left:238px;top:22px;width:330px;text-align:center;font-size:38px;color:var(--white);letter-spacing:.3px}
.headline-front .gold{color:var(--gold)}
.checklist{list-style:none;font-family:Lato,Arial,sans-serif;font-style:italic;font-size:13px;color:var(--ink)}
.checklist li{display:flex;align-items:center;height:22px;white-space:nowrap}
.checklist svg{margin-right:8px;flex:none}
.front-list{left:350px;top:134px}
.brand{font-family:"Bebas Neue",Impact,sans-serif;color:var(--green);text-align:center;line-height:.88}
.brand--front{left:400px;top:222px;width:160px;font-size:52px}
.brand--back{left:470px;top:175px;width:120px;font-size:40px}
.url-tab{left:142px;top:311px;width:230px;font-family:Roboto,Arial,sans-serif;font-weight:700;font-size:16px;color:var(--white);white-space:nowrap}
.follow{left:145px;top:352px;font-family:Roboto,Arial,sans-serif;font-weight:700;font-size:13px;color:var(--ink);white-space:nowrap}
.socials{left:145px;top:386px;display:flex;gap:24px;font-family:Roboto,Arial,sans-serif;font-size:11px;color:var(--white);white-space:nowrap}
.socials span{display:flex;align-items:center}
.socials span::before{content:"";width:9px;height:9px;background:var(--white);border-radius:2px;margin-right:6px}
.headline-back{left:228px;top:30px;width:365px;text-align:center}
.headline-back .l1{font-size:44px;color:var(--gold)}
.headline-back .l2{font-size:25px;color:var(--green);margin-top:2px}
.headline-back .l3{display:inline-block;margin-top:4px;background:var(--green);color:var(--white);font-size:19px;padding:4px 6px 2px}
.work-intro{left:235px;top:154px;font-family:Roboto,Arial,sans-serif;font-weight:700;font-size:13px;color:var(--ink)}
.back-list{left:235px;top:176px;font-size:12px}
.contact-name{left:48px;top:290px;font-family:Roboto,Arial,sans-serif;font-weight:700;font-size:20px;color:var(--ink)}
.contact-role{left:48px;top:314px;font-family:Roboto,Arial,sans-serif;font-weight:700;font-size:12.5px;color:var(--white)}
.contact-line{left:48px;display:flex;align-items:center;font-family:Roboto,Arial,sans-serif;font-weight:700;color:var(--white);white-space:nowrap}
.contact-line svg{margin-right:8px}
.contact-phone{top:346px;font-size:19px}
.contact-mail{top:374px;font-size:12.5px}
.cta{left:340px;top:290px;width:220px;text-align:center;font-family:Roboto,Arial,sans-serif;font-weight:700;font-size:13px;line-height:1.25;color:var(--ink)}
.cta-url{left:340px;top:377px;width:220px;text-align:center;font-family:Roboto,Arial,sans-serif;font-weight:700;font-size:13px;color:var(--white);white-space:nowrap}
</style>
</head>
<body>
<main class="canvas">

  <section class="card card--front" aria-label="Postcard front">
    <svg class="shapes" width="608" height="412" viewBox="0 0 608 412">
      <defs>
        <linearGradient id="goldSun" x1="0" y1="0" x2="0" y2="1">
          <stop offset="0" stop-color="#f9e08e"/><stop offset="1" stop-color="#e6a829"/>
        </linearGradient>
        <linearGradient id="headerGreen" x1="0" y1="0" x2="0" y2="1">
          <stop offset="0" stop-color="#1a8a43"/><stop offset="1" stop-color="#0b5a2a"/>
        </linearGradient>
      </defs>
      <circle cx="205" cy="318" r="172" fill="url(#goldSun)"/>
      <path d="M238 0H568V96Q568 112 552 112H254Q238 112 238 96Z" fill="url(#headerGreen)"/>
      <rect x="0" y="28" width="262" height="270" fill="var(--photo)" role="img" aria-label="Portrait photo of Mira Dabbot in a dark blazer"/>
      <path d="M110 300H372L380 342H110Z" fill="var(--green)"/>
      <rect y="345" width="608" height="28" fill="var(--gold)"/>
      <rect y="373" width="608" height="39" fill="var(--green-dark)"/>
      <rect x="34" y="262" width="68" height="132" fill="var(--book)" stroke="#c9d3c6" role="img" aria-label="Cover of the book The Coin Keeper"/>
    </svg>

    <h1 class="abs display headline-front">Get Instant Access to<br><span class="gold">Your Free Resources</span></h1>

    <ul class="abs checklist front-list">
      <li><svg width="14" height="14" viewBox="0 0 14 14"><rect x="1" y="3" width="10" height="10" fill="none" stroke="#e9b234" stroke-width="1.5"/><path d="M3 7l3 3 7-9" fill="none" stroke="#e9b234" stroke-width="2"/></svg>The Coin Keeper Checklist</li>
      <li><svg width="14" height="14" viewBox="0 0 14 14"><rect x="1" y="3" width="10" height="10" fill="none" stroke="#e9b234" stroke-width="1.5"/><path d="M3 7l3 3 7-9" fill="none" stroke="#e9b234" stroke-width="2"/></svg>Financial Worksheets</li>
      <li><svg width="14" height="14" viewBox="0 0 14 14"><rect x="1" y="3" width="10" height="10" fill="none" stroke="#e9b234" stroke-width="1.5"/><path d="M3 7l3 3 7-9" fill="none" stroke="#e9b234" stroke-width="2"/></svg>Database of Investment Tools</li>
    </ul>

    <div class="abs brand brand--front">The Coin<br>Keeper</div>

    <div class="abs url-tab">MiraDabbot.example/Resources</div>
    <p class="abs follow">Don't forget to follow Mira Dabbot on social media:</p>
    <div class="abs socials">
      <span>@thecoinkeeperbook</span>
      <span>@thecoinkeeperbook</span>
      <span>@CoinKeeperBook</span>
    </div>
  </section>

  <section class="card card--back" aria-label="Postcard back">
    <svg class="shapes" width="608" height="412" viewBox="0 0 608 412">
      <rect x="0" y="22" width="215" height="254" fill="var(--photo)" role="img" aria-label="Portrait photo of Mira Dabbot in a dark blazer"/>
      <path d="M0 275H230C290 275 300 300 340 300H608V340H0Z" fill="var(--gold)"/>
      <path d="M0 330H608V412H0Z" fill="var(--green)"/>
      <ellipse cx="452" cy="310" rx="135" ry="42" fill="var(--gold)"/>
      <path d="M440 350L452 360L464 350Z" fill="var(--gold)"/>
      <line x1="330" y1="352" x2="330" y2="405" stroke="#0b4f26" stroke-width="1.5"/>
    </svg>

    <h2 class="abs display headline-back">
      <div class="l1">Want to Work Directly</div>
      <div class="l2">With Mira and The Coin Keeper Team</div>
      <div class="l3">To Help You Make Your Money Grow and Stay Safe?</div>
    </h2>

    <p class="abs work-intro">Work with us to</p>
    <ul class="abs checklist back-list">
      <li><svg width="14" height="14" viewBox="0 0 14 14"><rect x="1" y="3" width="10" height="10" fill="none" stroke="#e9b234" stroke-width="1.5"/><path d="M3 7l3 3 7-9" fill="none" stroke="#e9b234" stroke-width="2"/></svg>Hire Mira as a Keynote Speaker</li>
      <li><svg width="14" height="14" viewBox="0 0 14 14"><rect x="1" y="3" width="10" height="10" fill="none" stroke="#e9b234" stroke-width="1.5"/><path d="M3 7l3 3 7-9" fill="none" stroke="#e9b234" stroke-width="2"/></svg>Teach Financial Literacy Workshops</li>
      <li><svg width="14" height="14" viewBox="0 0 14 14"><rect x="1" y="3" width="10" height="10" fill="none" stroke="#e9b234" stroke-width="1.5"/><path d="M3 7l3 3 7-9" fill="none" stroke="#e9b234" stroke-width="2"/></svg>Receive Financial Coaching</li>
    </ul>

    <div class="abs brand brand--back">The Coin<br>Keeper</div>

    <p class="abs contact-name">Mira Dabbot</p>
    <p class="abs contact-role">Author | Speaker | Investor</p>
    <p class="abs contact-line contact-phone"><svg width="18" height="18" viewBox="0 0 18 18"><circle cx="9" cy="9" r="8" fill="none" stroke="#fff" stroke-width="1.5"/><path d="M6 5l2 0 1 2-1 1q1 2 2 2l1-1 2 1 0 2q-5 0-7-7z" fill="#fff"/></svg>555-274-0381</p>
    <p class="abs contact-line contact-mail"><svg width="18" height="12" viewBox="0 0 18 12"><rect x="1" y="1" width="16" height="10" fill="none" stroke="#fff" stroke-width="1.5"/><path d="M1 1l8 6 8-6" fill="none" stroke="#fff" stroke-width="1.5"/></svg>mira@thecoinkeeperbook.example</p>

    <p class="abs cta">Want To Learn<br>More About<br>How We Can Help?</p>
    <p class="abs cta-url">MiraDabbot.example/Services</p>
  </section>

</main>
</body>
</html>
```